Business Card Design Project

We need a business card designed for a new Luxury Custom Homebuilding company based in Arizona. We previous were called "Belcrest Estates" but want to start using "Belcrest Custom Homes" We want the message to communicate high end, luxury and cutting-edge. We like the blue, white and black color scheme.
Belcrest Custom Homes
Marcus T. Halloway
Chief Executive Officer
Office: 480-555-0142
Mobile: 480-555-0178
email: marc@belcrestcustom-example.com
web adress: www.BelcrestCustom-example.com
Updates
We have made a change to our website address and email address based on recieving feedback from a nmber of individuals. The feedback was web address and email address was to long. Therefore we have made a change. The new web adress and email adress are the following.
www.BelcrestCustom-example.com
marc@belcrestcustom-example.com
Also I decided against using in yellow. I like the colors blue,black, white and maybe gray.
Target Market(s)
Our target market is the wealthy individuals looking for a luxury high-end custom home.
Industry/Entity Type
Business
Look and feel

```html
<!DOCTYPE html>
<html lang="en">
<head>
<meta charset="utf-8">
<title>Belcrest Custom Homes – Business Card</title>
<link rel="stylesheet" href="https://fonts.googleapis.com/css2?family=Roboto+Condensed:ital,wght@0,400;0,700;1,400&display=swap">
<style>
  :root {
    --card-blue: #5b9bd3;
    --ink-dark: #545456;
    --ink-light: #ffffff;
    --board-dark: #c9c9c9;
    --board-light: #f2f2f2;
  }
  * { box-sizing: border-box; margin: 0; padding: 0; }
  html, body {
    width: 1200px; height: 1200px; overflow: hidden;
  }
  body {
    position: relative;
    background: linear-gradient(90deg, var(--board-dark) 0%, var(--board-light) 45%, var(--board-light) 100%);
    font-family: "Roboto Condensed", "Arial Narrow", sans-serif;
  }
  .card {
    position: absolute;
    left: 114px;
    width: 970px;
    height: 553px;
    background: var(--card-blue);
    overflow: hidden;
  }
  .card--front { top: 22px; }
  .card--back  { top: 622px; }

  /* Front */
  .brand-name {
    position: absolute;
    left: 172px;
    top: 228px;
    color: var(--ink-dark);
    font-weight: 700;
    line-height: 1;
  }
  .brand-name__main { display: block; font-size: 104px; letter-spacing: -3px; }
  .brand-name__sub  { display: block; font-size: 36px; margin-top: 4px; letter-spacing: 0.5px; }

  .contact-frame {
    position: absolute;
    left: 541px;
    top: 228px;
    width: 383px;
    height: 274px;
    border-top: 2px solid var(--ink-light);
    border-left: 2px solid var(--ink-light);
  }
  .contact {
    position: absolute;
    left: 583px;
    top: 260px;
    color: var(--ink-light);
    font-size: 21px;
    line-height: 1.5;
  }
  .contact__name  { font-weight: 700; font-size: 23px; line-height: 1.4; }
  .contact__title { margin-bottom: 22px; }
  .contact__row   { display: flex; }
  .contact__label { width: 40px; }

  /* Back */
  .back-art { position: absolute; inset: 0; }
  .back-art text { font-family: "Roboto Condensed", "Arial Narrow", sans-serif; }
  .back-name { fill: var(--ink-light); font-weight: 700; }
  .back-url { font-size: 40px; fill: var(--ink-light); }
  .back-url__light { font-style: italic; font-weight: 400; }
  .back-url__bold  { font-weight: 700; }
  .back-url__dark  { font-weight: 700; fill: var(--ink-dark); }
</style>
</head>
<body>

  <section class="card card--front" aria-label="Card front">
    <div class="brand-name">
      <span class="brand-name__main">Belcrest</span>
      <span class="brand-name__sub">CUSTOM HOMES</span>
    </div>

    <div class="contact-frame"></div>
    <div class="contact">
      <p class="contact__name">Marcus T. Halloway</p>
      <p class="contact__title">Chief Executive Officer</p>
      <p class="contact__row"><span class="contact__label">P:</span>480-555-0142</p>
      <p class="contact__row"><span class="contact__label">M:</span>480-555-0178</p>
      <p class="contact__row"><span class="contact__label">E:</span>marc@belcrestcustom-example.com</p>
      <p class="contact__row"><span class="contact__label">W:</span>www.BelcrestCustom-example.com</p>
    </div>
  </section>

  <section class="card card--back" aria-label="Card back">
    <svg class="back-art" width="970" height="553" viewBox="0 0 970 553">
      <text class="back-name" x="25" y="345" font-size="290" textLength="918" lengthAdjust="spacingAndGlyphs">Belcrest</text>
      <text class="back-name" x="337" y="426" font-size="88" textLength="606" lengthAdjust="spacingAndGlyphs">CUSTOM HOMES</text>
      <text class="back-url" x="943" y="502" text-anchor="end"><tspan class="back-url__light">www.</tspan><tspan class="back-url__bold">Belcrest</tspan><tspan class="back-url__dark">Custom</tspan><tspan class="back-url__light">-example.com</tspan></text>
    </svg>
  </section>

</body>
</html>
```